Graphic Design for the Dravenor 10' Trade Show Booth

I need a trade show booth design for our ten foot booth.
The initial design should be based on 10 inches instead of ten feet. The winner will be expected to provide a ten foot print ready file. Please see the attached template.

Industry info: we are a Commercial Real Estate brokerage company
Imagery: Dravenor logo. also can have industrial buildings, people, icons...
Brand colors: 0c6dac Dark Blue; 5599c5 Light Blue; Gray 8a8585
Messaging:
We've Got Buyers
1031 Exchange
170 Exchange
Cash Sale
Attached you can find a few files: booth template, Dravenor Logo in EPS and AI formats.

Target Market(s)

Commercial real estate brokers looking for buyers - we deal with industrial buildings such as warehouses, factories, manufacturing and other commercial real estate.

Industry/Entity Type

Real Estate

Font styles to use
Sans Serif

Requirements
Must have
• Logo and messaging.
• Note, i have added several Lumo Vault images for you to see and if desired use in your designs. We have bought these images, so if you use them and your design is chosen, we can share them with you. Hi Teodoro,
• I have updated the design brief and added some Lumo Vault images for your use. If you like the images, you can use them and we have already purchased them. If you find other images on Lumo Vault, feel free to use the watermarked version and if your design is chosen, we can purchase the images.
Nice to have
• amazing look and feel. Could have images of buildings or people
Should not have
• No images of houses.

```html
<!DOCTYPE html>
<html lang="en">
<head>
<meta charset="utf-8">
<title>Dravenor Trade Show Booth</title>
<link rel="stylesheet" href="https://fonts.googleapis.com/css2?family=Montserrat:wght@600;700&display=swap">
<style>
  :root {
    --brand-dark: #1f2d63;
    --brand-blue: #0c6dac;
    --brand-light: #5599c5;
    --brand-gray: #8a8585;
    --panel-white: #f1f1f3;
    --headline: #ececef;
    --sky-top: #7fa3c9;
    --sky-low: #b9cde0;
    --building: #c9c0ae;
    --lawn: #7d8a4a;
  }
  * { margin: 0; padding: 0; box-sizing: border-box; }
  html, body { width: 1200px; height: 794px; overflow: hidden; background: var(--panel-white); }
  .booth {
    position: relative;
    width: 1200px;
    height: 794px;
    font-family: "Montserrat", sans-serif;
    background: var(--panel-white);
    overflow: hidden;
  }
  .booth-art { position: absolute; inset: 0; }
  .brand {
    position: absolute;
    left: 168px;
    top: 62px;
    display: flex;
    align-items: center;
    gap: 16px;
  }
  .brand-mark {
    width: 40px;
    height: 40px;
    background: var(--brand-gray);
  }
  .brand-name {
    font-size: 44px;
    font-weight: 600;
    color: var(--brand-blue);
    letter-spacing: 1px;
  }
  .message {
    position: absolute;
    left: 0;
    width: 100%;
    text-align: center;
    font-weight: 700;
    color: var(--headline);
    text-shadow: 0 2px 4px rgba(30, 40, 70, 0.35);
    line-height: 1;
    white-space: nowrap;
  }
  .message-lead { top: 180px; font-size: 80px; left: 12px; }
  .message-exchange-a { top: 300px; font-size: 68px; left: -20px; }
  .message-exchange-b { top: 385px; font-size: 68px; left: -40px; }
  .message-cash { top: 520px; font-size: 112px; left: -20px; }
</style>
</head>
<body>
<main class="booth">
  <svg class="booth-art" width="1200" height="794" viewBox="0 0 1200 794" xmlns="http://www.w3.org/2000/svg">
    <defs>
      <linearGradient id="sceneTones" x1="0" y1="0" x2="0" y2="1">
        <stop offset="0" stop-color="var(--sky-top)"/>
        <stop offset="0.35" stop-color="var(--sky-low)"/>
        <stop offset="0.5" stop-color="var(--building)"/>
        <stop offset="0.82" stop-color="#b3a995"/>
        <stop offset="0.9" stop-color="var(--lawn)"/>
        <stop offset="1" stop-color="#8e8c86"/>
      </linearGradient>
      <linearGradient id="baseBand" x1="0" y1="0" x2="1" y2="0">
        <stop offset="0" stop-color="var(--brand-blue)"/>
        <stop offset="1" stop-color="var(--brand-dark)"/>
      </linearGradient>
      <linearGradient id="topStripe" x1="0" y1="0" x2="1" y2="0">
        <stop offset="0" stop-color="var(--brand-dark)"/>
        <stop offset="0.8" stop-color="var(--brand-blue)"/>
        <stop offset="1" stop-color="var(--brand-dark)"/>
      </linearGradient>
    </defs>

    <rect class="booth-photo" x="0" y="150" width="1200" height="560" fill="url(#sceneTones)"
          role="img" aria-label="Photo of a large industrial warehouse with loading docks, trees and lawn under a blue sky"/>

    <path class="stripe-top" d="M0 140 L780 160 L985 110 L1200 175 L1200 195 L985 132 L780 182 L0 160 Z" fill="url(#topStripe)"/>
    <path class="panel-top" d="M0 0 H1200 V175 L985 110 L780 160 L0 140 Z" fill="var(--panel-white)"/>

    <rect class="band-base" x="150" y="700" width="1050" height="68" fill="url(#baseBand)"/>
    <path class="ribbon-left" d="M0 560 L150 630 L150 730 L0 640 Z" fill="var(--brand-blue)"/>
    <path class="ribbon-fold" d="M150 630 L170 700 L170 760 L150 730 Z" fill="var(--brand-light)"/>
    <path class="panel-corner" d="M0 640 L150 730 L170 760 L0 760 Z" fill="var(--panel-white)"/>
  </svg>

  <div class="brand">
    <span class="brand-mark"></span>
    <span class="brand-name">The Dravenor Group</span>
  </div>

  <p class="message message-lead">We've Got Buyers</p>
  <p class="message message-exchange-a">1031 Exchange</p>
  <p class="message message-exchange-b">170 Exchange</p>
  <p class="message message-cash">Cash Sale</p>
</main>
</body>
</html>
```